Brelvora company website, a website for employment for people with autism

The website will make a match between people and jobs, mainly in the graphical sector, but also other sectors.
The name of the company is brelvora and automates jobs with people that are on the autism spectrum.
The whole matchmaking and feedback process and so doesn't have to be in this prototype, we just want the general information pages and to convey a great look and brand identity that we will keep in the other pages to be developed. The website must be made with Wordpress, since the backend will be developed in Wordpress too.
It is a social project that wants to create possibilites for people with ASS to work from home for an employer or to do a variety of tasks for different customers.
The people we hire are generally not on the regular job market or have difficulty finding a job and "selling themselves"

Target Market(s)

matchmaking between talent (with ASS) and employers / jobs

Number of Pages Required

5+ page

Font styles to use
Sans Serif

Colors
ec1f27
e34298
a64599
6b449b
0355a3
0792cd

Requirements
Must have
• A stunning landing pages
• Integrate our logo and must match with what will do. We want a clean, modern, minimalistic, sleek website that radiates creativity and good looks.
• We have one page describing what we can do for customers, one page for people with ASS that would like to be candidates (our approach, learning program, ...), two pages that are addressed to partners who want to cooperate: the one's that can assist with autism related assistance and the one's that can help with the job coaching.
Nice to have
• In our logo are many colors as we embrace diversity and want to show that. Out main branding colors are red (for action) and blue for stability and will all gradients that go with it. Mainly white or black (or anthracite) for other parts
Should not have
• We want a modern and minimalistic design, no fluffy designs with lots of ornaments.

```html
<!DOCTYPE html>
<html lang="en">
<head>
<meta charset="utf-8">
<title>Brelvora – Work that fits you</title>
<link href="https://fonts.googleapis.com/css2?family=Open+Sans:ital,wght@0,400;0,600;0,700;0,800;1,400&display=swap" rel="stylesheet">
<style>
:root{
  --pink:#e0288f;
  --magenta:#c2368f;
  --violet:#6b449b;
  --blue:#2a6bb5;
  --navy:#1d3f8f;
  --cyan:#0792cd;
  --ink:#1b1b22;
  --text:#333;
  --muted:#8a8a95;
  --lilac:#dcdcec;
  --blush:#f6dbe8;
  --white:#fff;
  --grad:linear-gradient(135deg,var(--pink) 0%,var(--violet) 55%,var(--blue) 100%);
}
*{margin:0;padding:0;box-sizing:border-box}
html,body{width:1200px;height:3947px;overflow:hidden;background:var(--white)}
body{font-family:"Open Sans",Arial,sans-serif;color:var(--text);position:relative}
.abs{position:absolute}

/* nav */
.nav-link{position:absolute;top:36px;font-size:15px;font-weight:700;letter-spacing:1.5px;color:var(--ink);text-transform:uppercase}
.nav-home{left:124px;color:var(--ink)}
.nav-home-mark{position:absolute;left:117px;top:22px}
.brand-tab{position:absolute;left:526px;top:0;width:148px;height:134px;z-index:3}
.brand-dot{position:absolute;left:578px;top:14px;width:44px;height:44px;border-radius:50%;background:var(--pink);z-index:4}
.brand-name{position:absolute;left:526px;width:148px;top:68px;text-align:center;font-size:17px;font-weight:700;letter-spacing:2px;color:var(--ink);z-index:4}

/* hero */
.hero{position:absolute;left:0;top:80px;width:1200px;height:533px;
  background:radial-gradient(circle at 55% 10%,#9fe7ff 0%,rgba(120,200,255,.4) 18%,transparent 40%),
             radial-gradient(circle at 52% 45%,#5fd08a 0%,rgba(60,160,170,.6) 14%,transparent 30%),
             linear-gradient(110deg,#e02d96 0%,#a23aa6 35%,#4b3fa8 65%,#1f3e9a 100%)}
.play{position:absolute;left:560px;top:310px}

/* search */
.search{position:absolute;left:210px;top:587px;width:780px;height:89px;background:var(--white);
  box-shadow:0 14px 26px -6px rgba(7,146,205,.55);z-index:2}
.field{position:absolute;top:23px;height:40px;background:#e9e9ee;font-size:12px;font-style:italic;color:#666;padding:11px 18px}
.field-select::after{content:"";position:absolute;right:14px;top:17px;border:6px solid transparent;border-top-color:#555}
.search-btn{position:absolute;left:650px;top:23px;width:114px;height:40px;background:var(--navy);color:var(--white);font-size:13px;font-weight:700;text-align:center;line-height:40px}

/* section heads */
.eyebrow{position:absolute;left:0;width:1200px;text-align:center;font-size:14px;letter-spacing:.5px;color:var(--ink);text-transform:uppercase}
.heading{position:absolute;left:0;width:1200px;text-align:center;font-size:46px;font-weight:800;color:var(--ink);letter-spacing:.5px;line-height:1}
.lead{position:absolute;left:300px;width:600px;text-align:center;font-size:15px;line-height:24px;color:var(--ink)}

/* process hexagons */
.hex{position:absolute;width:297px;height:342px;clip-path:polygon(50% 0,100% 25%,100% 75%,50% 100%,0 75%,0 25%);
  background:var(--grad);color:var(--white);text-align:center}
.hex-title{position:absolute;left:0;width:100%;font-size:17px;font-weight:800;line-height:27px;text-transform:uppercase}
.hex-outline{position:absolute;left:463px;top:966px;width:298px;height:344px}
.hex-outline-text{position:absolute;left:493px;width:238px;text-align:center;color:var(--ink)}
.apply-btn{position:absolute;left:71px;top:114px;width:155px;height:42px;border:2px solid var(--white);font-size:14px;font-weight:600;letter-spacing:2px;line-height:38px}

/* project */
.project-copy{position:absolute;left:118px;top:2108px;width:430px;font-size:15px;line-height:34px;color:var(--ink)}
.btn-pill{position:absolute;left:126px;top:2300px;width:156px;height:42px;border-radius:12px;background:var(--pink);color:var(--white);
  font-size:14px;font-weight:700;letter-spacing:1.5px;line-height:42px;text-align:center;box-shadow:0 10px 18px -4px rgba(224,40,143,.45)}

/* testimonials */
.card{position:absolute;top:3006px;width:312px;height:223px;background:var(--white);border-radius:8px;
  box-shadow:0 4px 14px rgba(60,60,120,.18);text-align:center;padding:68px 24px 0}
.card-name{font-size:13px;font-weight:700;color:var(--ink);text-transform:uppercase;margin-bottom:10px}
.card-text{font-size:12px;line-height:20px;color:var(--muted)}
.avatar{position:absolute;top:-38px;left:114px;width:84px;height:84px;border-radius:50%;border:4px solid var(--white);
  box-shadow:0 0 0 3px var(--magenta)}

/* profile */
.contact-ring{position:absolute;top:3482px;width:144px;height:144px}
.contact-text{position:absolute;top:3648px;width:320px;text-align:center;font-size:20px;line-height:30px;color:var(--ink);text-transform:uppercase}
.social{position:absolute;top:3782px;left:0;width:1200px;text-align:center;font-size:13px;font-weight:600;color:var(--violet)}
.social span{margin:0 12px}
.copyright{position:absolute;top:3906px;left:0;width:1200px;text-align:center;font-size:11px;color:var(--ink)}
</style>
</head>
<body>

<!-- decorative background shapes -->
<svg class="abs" style="left:0;top:0" width="1200" height="3947" aria-hidden="true">
  <g fill="none" stroke="var(--lilac)" stroke-width="10">
    <polygon points="250,790 220,842 280,842"/>
    <polygon points="300,1580 250,1700 350,1700"/>
    <polygon points="90,1905 55,1935 110,1960"/>
    <polygon points="250,2580 220,2625 280,2625"/>
    <polygon points="1180,900 1150,1000 1200,1000"/>
  </g>
  <g fill="none" stroke="var(--blush)" stroke-width="8">
    <polygon points="1190,2700 1150,2780 1200,2780"/>
    <polygon points="90,3440 55,3470 105,3500"/>
    <polygon points="710,3385 690,3420 730,3420"/>
  </g>
  <circle cx="40" cy="1115" r="45" fill="var(--lilac)" opacity=".6"/>
  <circle cx="942" cy="1424" r="46" fill="var(--lilac)" opacity=".6"/>
  <circle cx="1012" cy="696" r="24" fill="var(--lilac)" opacity=".7"/>
  <circle cx="1054" cy="1804" r="24" fill="var(--blush)"/>
  <circle cx="40" cy="2893" r="52" fill="var(--blush)"/>
  <circle cx="1054" cy="3340" r="24" fill="var(--blush)"/>
  <circle cx="133" cy="3687" r="24" fill="var(--blush)"/>
  <circle cx="1190" cy="3770" r="80" fill="var(--blush)" opacity=".8"/>
  <polygon points="300,3350 292,3366 308,3366" fill="var(--blush)"/>
</svg>

<!-- navigation -->
<svg class="nav-home-mark" width="58" height="40" aria-hidden="true"><polygon points="29,2 55,14 55,28 29,38 3,28 3,14" fill="none" stroke="var(--violet)" stroke-width="2"/></svg>
<a class="nav-link nav-home">Home</a>
<a class="nav-link" style="left:224px">About us</a>
<a class="nav-link" style="left:360px">Jobs</a>
<a class="nav-link" style="left:784px">Blog</a>
<a class="nav-link" style="left:871px">Contact</a>
<a class="nav-link" style="left:997px">Apply now</a>

<svg class="brand-tab" viewBox="0 0 148 134" aria-hidden="true"><polygon points="0,0 148,0 148,100 74,134 0,100" fill="#fff"/></svg>
<div class="brand-dot"></div>
<div class="brand-name">BRELVORA</div>

<!-- hero -->
<div class="hero" role="img" aria-label="Colourful smoke cloud on a pink-to-blue gradient backdrop"></div>
<svg class="play" width="86" height="86" aria-label="Play video">
  <circle cx="43" cy="43" r="40" fill="none" stroke="#fff" stroke-width="3"/>
  <polygon points="35,27 61,43 35,59" fill="none" stroke="#fff" stroke-width="3"/>
</svg>

<!-- search -->
<div class="search">
  <div class="field" style="left:19px;width:189px">Job Key Word</div>
  <div class="field field-select" style="left:227px;width:192px">New York, CA</div>
  <div class="field field-select" style="left:440px;width:192px">Graphic Design</div>
  <div class="search-btn">Search</div>
</div>

<!-- process -->
<div class="eyebrow" style="top:765px">Our process</div>
<h2 class="heading" style="top:798px">HOW WE WORK FOR YOU?</h2>
<p class="lead" style="top:858px">Lorem ipsum dolor sit amet, consectetur adipisicing elit, sed do eiusmod tempor incididunt ut labore et dolore magna aliqua</p>

<div class="hex" style="left:116px;top:966px">
  <svg class="abs" style="left:112px;top:76px" width="72" height="72" aria-hidden="true">
    <circle cx="30" cy="28" r="18" fill="none" stroke="#fff" stroke-width="6"/>
    <line x1="43" y1="41" x2="64" y2="62" stroke="#fff" stroke-width="8" stroke-linecap="round"/>
  </svg>
  <div class="hex-title" style="top:164px">Searching for<br>the best job</div>
</div>

<svg class="hex-outline" viewBox="0 0 298 344" aria-hidden="true">
  <defs><linearGradient id="hexStroke" x1="0" y1="0" x2="1" y2="1"><stop offset="0" stop-color="#e0288f"/><stop offset="1" stop-color="#2a6bb5"/></linearGradient></defs>
  <polygon points="149,2 296,87 296,257 149,342 2,257 2,87" fill="#fff" stroke="url(#hexStroke)" stroke-width="3"/>
</svg>
<div class="hex-outline-text" style="top:1052px;font-size:17px;font-weight:800;line-height:27px">APPLY ONLINE NOW<br>TO GET PRIOR JOBS</div>
<div class="hex-outline-text" style="top:1132px;left:523px;width:178px;font-size:14px;line-height:21px">Lorem ipsum dolor sit amet, consectetur adipisicing elit, sed</div>

<div class="hex" style="left:808px;top:966px">
  <svg class="abs" style="left:112px;top:68px" width="80" height="76" aria-hidden="true" fill="none" stroke="#fff" stroke-width="3">
    <rect x="4" y="20" width="50" height="38" rx="3"/>
    <circle cx="29" cy="34" r="7"/>
    <path d="M18 54c2-8 20-8 22 0"/>
    <line x1="0" y1="64" x2="60" y2="64"/>
    <rect x="44" y="4" width="32" height="22" rx="3"/>
    <polyline points="52,26 50,32 58,26"/>
  </svg>
  <div class="hex-title" style="top:164px">Face interview<br>online</div>
</div>

<div class="hex" style="left:464px;top:1308px;background:linear-gradient(135deg,var(--navy) 0%,var(--violet) 50%,var(--pink) 100%)">
  <div class="apply-btn">APPLY NOW</div>
  <svg class="abs" style="left:118px;top:196px" width="64" height="80" aria-hidden="true" fill="none" stroke="#fff" stroke-width="3" stroke-linecap="round">
    <line x1="26" y1="4" x2="26" y2="12"/><line x1="10" y1="12" x2="15" y2="17"/><line x1="42" y1="12" x2="37" y2="17"/>
    <path d="M22 56V26a4 4 0 0 1 8 0v20l14 4c5 1 8 6 7 11l-3 14H26L14 58a4 4 0 0 1 6-6z"/>
  </svg>
</div>

<!-- project -->
<div class="eyebrow" style="top:1774px">Our project</div>
<h2 class="heading" style="top:1806px">SELLING THEMSELVES</h2>
<p class="lead" style="top:1870px;left:340px;width:520px">Lorem ipsum dolor sit amet, consectetur adipisicing elit, sed do eiusmod tempor incididunt ut labore et dolore magna aliqua</p>

<p class="project-copy">Sed ut perspiciatis unde omnis iste natus error sit voluptatem accusantium doloremque laudantium, totam rem aperiam, eaque ipsa quae ab illo inventore veritatis et quasi architecto beatae.</p>
<div class="btn-pill">VIEW MORE</div>

<svg class="abs" style="left:584px;top:1921px" width="616" height="758" viewBox="0 0 616 758">
  <defs>
    <linearGradient id="projGrad" x1="0" y1="0" x2="1" y2="1"><stop offset="0" stop-color="#e0288f"/><stop offset=".5" stop-color="#a64599"/><stop offset="1" stop-color="#2a6bb5"/></linearGradient>
    <linearGradient id="teamTone" x1="0" y1="0" x2="1" y2="1"><stop offset="0" stop-color="#d9d2c6"/><stop offset="1" stop-color="#8a7566"/></linearGradient>
    <linearGradient id="portraitTone" x1="0" y1="0" x2="0" y2="1"><stop offset="0" stop-color="#7d6a58"/><stop offset="1" stop-color="#1f2a4a"/></linearGradient>
  </defs>
  <polygon points="140,30 253,95 253,225 140,290 27,225 27,95" fill="none" stroke="#bfe0f2" stroke-width="3"/>
  <polygon points="310,0 526,125 526,375 310,500 94,375 94,125" fill="url(#teamTone)" role="img" aria-label="Photo of smiling colleagues sharing coffee in an office"/>
  <polygon points="115,240 262,325 262,495 115,580 -32,495 -32,325" fill="url(#portraitTone)" role="img" aria-label="Photo of a smiling young man in a suit and tie"/>
  <polygon points="470,224 701,357 701,624 470,758 239,624 239,357" fill="url(#projGrad)" opacity=".88"/>
</svg>

<!-- testimonials -->
<div class="eyebrow" style="top:2767px">Testimonials</div>
<h2 class="heading" style="top:2800px">WHAT CLIENT SAYS</h2>
<p class="lead" style="top:2865px;left:340px;width:520px">Lorem ipsum dolor sit amet, consectetur adipisicing elit, sed do eiusmod tempor incididunt ut labore et dolore magna aliqua</p>

<div class="card" style="left:121px">
  <div class="avatar" role="img" aria-label="Portrait of the client" style="background:linear-gradient(160deg,#6e8aa6,#b78a5a)"></div>
  <div class="card-name">Maren Holt</div>
  <p class="card-text">Today I want to tell you about my first week at my new job. The team is kind and patient, and the work fits my skills well. I finally feel at home here.</p>
</div>
<div class="card" style="left:460px">
  <div class="avatar" role="img" aria-label="Portrait of the client" style="background:linear-gradient(160deg,#8fb3d9,#c9a07a)"></div>
  <div class="card-name">Ines Varga</div>
  <p class="card-text">Working from home with clear tasks was exactly what I needed. Short, calm calls with my coach every week keep me on track and help me plan each project step by step.</p>
</div>
<div class="card" style="left:797px">
  <div class="avatar" role="img" aria-label="Portrait of the client" style="background:linear-gradient(160deg,#5a5a66,#a3826a)"></div>
  <div class="card-name">Ines Varga</div>
  <p class="card-text">After my training, my employer and I were matched on a design project. It was an unforgettable start. We meet online and I work at my own pace.</p>
</div>

<!-- profile -->
<div class="eyebrow" style="top:3338px">More about us</div>
<h2 class="heading" style="top:3370px">PROFILE</h2>

<svg width="0" height="0" class="abs" aria-hidden="true">
  <defs><linearGradient id="ringGrad" x1="0" y1="0" x2="1" y2="1"><stop offset="0" stop-color="#e0288f"/><stop offset="1" stop-color="#1d3f8f"/></linearGradient></defs>
</svg>

<svg class="contact-ring" style="left:202px" viewBox="0 0 144 144" aria-label="Address">
  <circle cx="72" cy="72" r="69" fill="none" stroke="url(#ringGrad)" stroke-width="4"/>
  <g fill="none" stroke="url(#ringGrad)" stroke-width="3">
    <path d="M72 88s-16-18-16-30a16 16 0 0 1 32 0c0 12-16 30-16 30z"/><circle cx="72" cy="58" r="6"/>
    <ellipse cx="72" cy="92" rx="22" ry="6"/>
  </g>
</svg>
<svg class="contact-ring" style="left:531px" viewBox="0 0 144 144" aria-label="Phone">
  <circle cx="72" cy="72" r="69" fill="none" stroke="url(#ringGrad)" stroke-width="4"/>
  <g fill="none" stroke="url(#ringGrad)" stroke-width="3" stroke-linejoin="round">
    <rect x="56" y="44" width="32" height="54" rx="5"/><line x1="56" y1="54" x2="88" y2="54"/><line x1="56" y1="86" x2="88" y2="86"/><circle cx="72" cy="92" r="2"/>
  </g>
</svg>
<svg class="contact-ring" style="left:860px" viewBox="0 0 144 144" aria-label="Email">
  <circle cx="72" cy="72" r="69" fill="none" stroke="url(#ringGrad)" stroke-width="4"/>
  <g fill="none" stroke="url(#ringGrad)" stroke-width="3" stroke-linejoin="round">
    <rect x="46" y="56" width="52" height="36"/><polyline points="46,56 72,78 98,56"/>
  </g>
</svg>

<div class="contact-text" style="left:114px">418 Harrow Lane<br>Ferndale, OR 97214</div>
<div class="contact-text" style="left:443px">555 - 24 - 718<br>310 - 62 - 945</div>
<div class="contact-text" style="left:772px">mail@brelvora.be<br>jobs@brelvora.be</div>

<div class="social"><span>Sharepond</span><span>Snapfold</span><span>Chirpline</span><span>Workmesh</span></div>

<div class="copyright">Copyright 2019. All rights reserved</div>

</body>
</html>
```